Real Estate For Sale Signage

I'm an independent agent in Lismore NSW Australia with high standards and looking for a catching 'For Sale'sign board.
I like classy, elegant, stylish and simple best.
My colours are red, white and black.
I don't have a logo or other font designs I need to stick to. I like the concept of a house or real estate design.
Before I created this project I played around on publisher and created the PDF attached. I'm not sold on it, but I don't mind the way the name has been layed out. Originally I had a white background with black & red font.
Fancy fonts for my name would be nice, but must not be busy.
Updates

Just wanted to advise that I have updated my brief and used the tools available to help get my ideas through.

Thank you for your work and time.

Kind regards
Marella

Industry/Entity Type

Real Estate

Requirements
Must have
• For Sale
Marella Quint Real Estate (must stand out)
0400 517 382 (must stand out)
17 Tallowood Street North Lismore
www.marellaquintrealestate.com.au

```html
<!DOCTYPE html>
<html lang="en">
<head>
<meta charset="utf-8">
<title>Marella Quint Real Estate – For Sale</title>
<link rel="stylesheet" href="https://fonts.googleapis.com/css2?family=Anton&family=Marcellus&family=Questrial&display=swap">
<style>
  :root {
    --sign-red: #ff0000;
    --sign-white: #ffffff;
  }
  html, body {
    margin: 0;
    padding: 0;
    width: 900px;
    height: 1200px;
    overflow: hidden;
    background: var(--sign-white);
  }
  .sign {
    position: relative;
    width: 900px;
    height: 1200px;
    background: var(--sign-white);
    overflow: hidden;
  }
  .headline {
    position: absolute;
    left: 0;
    top: 0;
    width: 900px;
    height: 320px;
  }
  .headline text {
    font-family: "Anton", "Oswald", sans-serif;
    fill: var(--sign-red);
  }
  .flourish-band {
    position: absolute;
    left: 0;
    top: 440px;
    width: 900px;
    height: 180px;
    background: linear-gradient(to bottom, rgba(255,0,0,0) 0%, rgba(255,0,0,0.35) 40%, var(--sign-red) 100%);
  }
  .red-field {
    position: absolute;
    left: 0;
    top: 618px;
    width: 900px;
    height: 582px;
    background: var(--sign-red);
  }
  .rule {
    position: absolute;
    left: 24px;
    width: 852px;
    height: 3px;
    background: var(--sign-white);
  }
  .rule--top { top: 674px; }
  .rule--bottom { top: 814px; }
  .agency-name,
  .agency-type,
  .phone,
  .address,
  .website {
    position: absolute;
    left: 0;
    width: 900px;
    margin: 0;
    text-align: center;
    color: var(--sign-white);
    white-space: nowrap;
  }
  .agency-name {
    top: 680px;
    font-family: "Marcellus", serif;
    font-size: 104px;
    line-height: 130px;
    font-weight: 400;
  }
  .agency-type {
    top: 830px;
    font-family: "Marcellus", serif;
    font-size: 78px;
    line-height: 100px;
  }
  .phone {
    top: 958px;
    font-family: "Questrial", sans-serif;
    font-size: 84px;
    line-height: 100px;
    letter-spacing: 6px;
  }
  .address {
    top: 1074px;
    font-family: "Questrial", sans-serif;
    font-size: 33px;
    line-height: 44px;
  }
  .website {
    top: 1118px;
    font-family: "Questrial", sans-serif;
    font-size: 33px;
    line-height: 44px;
  }
</style>
</head>
<body>
  <main class="sign">
    <svg class="headline" viewBox="0 0 900 320" width="900" height="320">
      <text x="450" y="270" text-anchor="middle" font-size="232" textLength="828" lengthAdjust="spacingAndGlyphs">FOR SALE</text>
    </svg>

    <div class="flourish-band" role="img" aria-label="Red swirling floral ornament rising from the red lower field"></div>
    <div class="red-field"></div>

    <div class="rule rule--top"></div>
    <h1 class="agency-name">Marella Quint</h1>
    <div class="rule rule--bottom"></div>
    <p class="agency-type">Real Estate</p>
    <p class="phone">0400 517 382</p>
    <p class="address">17 Tallowood Street North Lismore</p>
    <p class="website">www.marellaquintrealestate.com.au</p>
  </main>
</body>
</html>
```